Powerpoint Presentation (urgent)

We need a powerpoint presentation to accompany our other pitch materials for a really exciting, new project.

It is a project related to gaming.

The presentation should be engaging, professionally done, and be trendy and captivating.

```html
<!DOCTYPE html>
<html lang="en">
<head>
<meta charset="utf-8">
<title>Gaming Pitch Deck – Slide Overview</title>
<link rel="stylesheet" href="https://fonts.googleapis.com/css2?family=Arimo:wght@400;700&family=Open+Sans:wght@400;600&display=swap">
<style>
  :root{
    --canvas:#e8e8e8;
    --teal:#17a89a;
    --teal-dark:#0f9486;
    --teal-mid:#6fc2b8;
    --teal-light:#a7d9d3;
    --teal-pale:#cfe9e5;
    --teal-faint:#e6f4f2;
    --white:#ffffff;
    --grey-head:#8c8c8c;
    --grey-text:#5e5e5e;
    --grey-soft:#9a9a9a;
  }
  *{box-sizing:border-box;margin:0;padding:0}
  html,body{width:1200px;height:1200px;overflow:hidden;background:var(--canvas)}
  .canvas{position:relative;width:1200px;height:1200px}
  .slide{position:absolute;width:365px;height:273px;background:var(--white);overflow:hidden;font-family:"Arimo",Arial,sans-serif}
  .slide--teal{background:linear-gradient(160deg,#19ad9f 0%,#15a294 100%)}
  .top-strip{position:absolute;left:0;top:0;width:100%;height:8px;display:flex}
  .top-strip span{flex:1}
  .top-strip span:nth-child(1){background:var(--teal-light)}
  .top-strip span:nth-child(2){background:var(--teal-pale)}
  .top-strip span:nth-child(3){background:var(--teal)}
  .slide--teal .top-strip{opacity:.75}
  .slide--teal .top-strip span:nth-child(3){background:var(--teal-dark)}

  .heading{position:absolute;left:0;right:0;top:22px;text-align:center;font-weight:700;font-size:21px;color:var(--grey-head)}
  .rule{position:absolute;left:21px;right:21px;top:56px;height:1px;background:var(--teal)}
  .footer-rule{position:absolute;left:21px;right:26px;top:254px;height:1px;background:var(--teal)}
  .page-no{position:absolute;right:18px;top:250px;width:8px;height:8px;background:var(--teal);color:var(--white);font-size:5px;line-height:8px;text-align:center}

  /* Title slide */
  .brand{position:absolute;left:13px;top:22px;display:flex;align-items:center;gap:6px;color:var(--white);font-size:12px}
  .brand i{width:18px;height:18px;border-radius:50%;background:var(--white);display:block}
  .title-block{position:absolute;left:163px;top:112px;color:var(--white)}
  .title-block h1{font-size:21px;font-weight:700;line-height:1.2}
  .title-block p{font-size:20px;line-height:1.2}

  /* Cards */
  .card{position:absolute;top:76px;width:94px;height:130px;border:3px solid;background:var(--white)}
  .card h3{height:22px;margin:-3px -3px 0;color:var(--white);font-weight:400;font-size:13px;line-height:24px;text-align:center}
  .card svg{display:block;margin:10px auto 0}
  .card .dash{margin:6px 10px 0;border-top:1px dashed #bbb}
  .card .label{margin-top:9px;text-align:center;font-size:9px;color:var(--grey-soft)}
  .card .tiny{margin:2px 8px 0;text-align:center;font-family:"Open Sans",sans-serif;font-size:3.6px;line-height:1.45;color:var(--grey-soft)}
  .card--light{border-color:var(--teal-light)} .card--light h3{background:var(--teal-light)}
  .card--mid{border-color:var(--teal-mid)} .card--mid h3{background:var(--teal-mid)}
  .card--dark{border-color:var(--teal)} .card--dark h3{background:var(--teal)}

  /* Text slide */
  .subhead{position:absolute;left:19px;top:77px;font-family:"Open Sans",sans-serif;font-weight:600;font-size:10px;color:var(--teal)}
  .body-copy{position:absolute;left:19px;top:97px;width:322px;font-family:"Open Sans",sans-serif;font-size:8.4px;line-height:16.6px;color:var(--grey-text)}

  /* Hexagon slide */
  .callout{position:absolute;font-size:9px;line-height:1.05}
  .callout b{display:block;color:var(--teal);font-weight:700}
  .callout span{color:var(--grey-soft);font-size:7.5px}

  /* Stats slide */
  .map-area{position:absolute;left:30px;top:76px;width:300px;height:85px;background:radial-gradient(ellipse at center,#f1f4f4 0%,rgba(241,244,244,0) 75%)}
  .stat{position:absolute;top:90px;width:100px}
  .stat svg{position:absolute}
  .stat .pct{position:absolute;width:54px;text-align:center;top:20px;color:var(--teal);font-size:13px}
  .stat p{position:absolute;top:68px;left:0;width:100px;font-family:"Open Sans",sans-serif;font-size:6.3px;line-height:9.7px;color:var(--grey-text)}

  /* Section slide */
  .band{position:absolute;left:0;right:0;top:99px;height:79px;background:var(--white);text-align:center}
  .band h2{margin-top:13px;color:var(--teal);font-size:21px;font-weight:700;line-height:1.2}
  .band p{color:var(--grey-head);font-size:20px;line-height:1.2}
  .page-plain{position:absolute;right:20px;top:250px;color:var(--white);font-size:6px}

  /* Closing slide */
  .thanks{position:absolute;left:0;right:0;top:94px;text-align:center;color:var(--white);font-size:32px}
  .thanks-bar{position:absolute;left:83px;top:151px;width:198px;height:6px;display:flex}
  .thanks-bar span{flex:1}
  .thanks-bar span:nth-child(1){background:#129a8c}
  .thanks-bar span:nth-child(2){background:#1fb3a4}
  .thanks-bar span:nth-child(3){background:#0c8a7d}
</style>
</head>
<body>
<div class="canvas">

  <section class="slide slide--teal" style="left:24px;top:166px" role="img" aria-label="Teal title slide with faint connected-node network pattern">
    <div class="top-strip"><span></span><span></span><span></span></div>
    <div class="brand"><i></i>Logo</div>
    <div class="title-block"><h1>Presentation Title</h1><p>Subtitle</p></div>
  </section>

  <section class="slide" style="left:418px;top:166px">
    <div class="top-strip"><span></span><span></span><span></span></div>
    <h2 class="heading">Heading Goes Here</h2>
    <div class="rule"></div>
    <div class="card card--light" style="left:29px">
      <h3>Subheading</h3>
      <svg width="28" height="24" viewBox="0 0 28 24" fill="none" stroke="#aaa" stroke-width="0.8"><rect x="2" y="2" width="24" height="15"/><path d="M11 17v4h6v-4M9 21h10"/></svg>
      <div class="dash"></div>
      <div class="label">HEADLINE</div>
      <div class="tiny">Lorem ipsum dolor sit amet, consectetur adipiscing elit, sed do eiusmod tempor.</div>
    </div>
    <div class="card card--mid" style="left:135px">
      <h3>Subheading</h3>
      <svg width="28" height="24" viewBox="0 0 28 24" fill="none" stroke="#aaa" stroke-width="0.8"><path d="M3 22V12M7 22V4M11 22V14M15 22V8M19 22V16M23 22V10"/></svg>
      <div class="dash"></div>
      <div class="label">HEADLINE</div>
      <div class="tiny">Lorem ipsum dolor sit amet, consectetur adipiscing elit, sed do eiusmod tempor.</div>
    </div>
    <div class="card card--dark" style="left:241px">
      <h3>Subheading</h3>
      <svg width="28" height="24" viewBox="0 0 28 24" fill="none" stroke="#aaa" stroke-width="0.8"><rect x="3" y="2" width="17" height="13"/><rect x="6" y="5" width="17" height="13" fill="#fff"/><rect x="9" y="8" width="17" height="13" fill="#fff"/></svg>
      <div class="dash"></div>
      <div class="label">HEADLINE</div>
      <div class="tiny">Lorem ipsum dolor sit amet, consectetur adipiscing elit, sed do eiusmod tempor.</div>
    </div>
    <div class="footer-rule"></div><div class="page-no">1</div>
  </section>

  <section class="slide" style="left:810px;top:166px">
    <div class="top-strip"><span></span><span></span><span></span></div>
    <h2 class="heading">Heading Goes Here</h2>
    <div class="rule"></div>
    <h3 class="subhead">Sub-Heading 1</h3>
    <p class="body-copy">It is a long established fact that a reader will be distracted by the readable content of a page when looking at its layout. The point of using Lorem Ipsum is that it has a more-or-less normal distribution of letters, as opposed to using 'Content here, content here', making it look li model text, and a search for 'lorem ipsum' will uncover many web sites still in their infancy. Various versions have evolved over the years, sometimes by accident, sometimes on purpose (injected humour and the like).</p>
    <div class="footer-rule"></div><div class="page-no">2</div>
  </section>

  <section class="slide" style="left:24px;top:468px">
    <div class="top-strip"><span></span><span></span><span></span></div>
    <h2 class="heading">Heading Goes Here</h2>
    <div class="rule"></div>
    <svg style="position:absolute;left:0;top:0" width="365" height="273" viewBox="0 0 365 273">
      <g transform="translate(180 140)">
        <polygon points="0,0 -59,-34 0,-68" fill="#8dcdc5"/>
        <polygon points="0,0 0,-68 59,-34" fill="#17a89a"/>
        <polygon points="0,0 59,-34 59,34" fill="#5cb9ae"/>
        <polygon points="0,0 59,34 0,68" fill="#7cc4bb"/>
        <polygon points="0,0 0,68 -59,34" fill="#cfe9e5"/>
        <polygon points="0,0 -59,34 -59,-34" fill="#e3f2f0"/>
        <g fill="none" stroke="#fff" stroke-width="0.9">
          <rect x="-26" y="-45" width="10" height="13"/><circle cx="-14" cy="-45" r="3.5"/>
          <circle cx="14" cy="-43" r="4"/><path d="M17 -40l5 5"/>
          <circle cx="38" cy="0" r="6"/><path d="M35 -2h6M35 0h6M35 2h6"/>
          <rect x="10" y="30" width="10" height="13"/><path d="M12 34h6M12 37h6M12 40h6"/>
          <rect x="-29" y="31" width="14" height="9"/><path d="M-29 31l7 5l7-5"/>
          <circle cx="-38" cy="0" r="6"/><path d="M-38 -3v3h3"/>
        </g>
      </g>
      <g fill="none" stroke="#9a9a9a" stroke-width="0.7" stroke-dasharray="3 2">
        <path d="M91 77h35l6 6"/><path d="M228 83l6-6h36"/>
        <path d="M86 141h22"/><path d="M251 141h22"/>
        <path d="M91 201h38l6-6"/><path d="M224 195l6 6h38"/>
      </g>
    </svg>
    <div class="callout" style="left:44px;top:70px"><b>Headline</b><span>Description</span></div>
    <div class="callout" style="left:276px;top:70px"><b>Headline</b><span>Description</span></div>
    <div class="callout" style="left:44px;top:134px"><b>Headline</b><span>Description</span></div>
    <div class="callout" style="left:276px;top:134px"><b>Headline</b><span>Description</span></div>
    <div class="callout" style="left:44px;top:194px"><b>Headline</b><span>Description</span></div>
    <div class="callout" style="left:276px;top:194px"><b>Headline</b><span>Description</span></div>
    <div class="footer-rule"></div><div class="page-no">3</div>
  </section>

  <section class="slide" style="left:418px;top:468px">
    <div class="top-strip"><span></span><span></span><span></span></div>
    <h2 class="heading">Heading Goes Here</h2>
    <div class="rule"></div>
    <div class="map-area" role="img" aria-label="Faint world map behind the statistics"></div>
    <div class="stat" style="left:31px">
      <svg width="54" height="54" viewBox="0 0 54 54" style="left:14px;top:0"><circle cx="27" cy="27" r="25" fill="none" stroke="#17a89a" stroke-width="1.8" stroke-dasharray="110 47" transform="rotate(-80 27 27)"/></svg>
      <div class="pct" style="left:14px">30%</div>
      <p>It is a long established fact that a reader will be distracted by the readable content of a page. The point of using Lorem Ipsum is that it has a more-or-less distribution of letters, as opposed to using 'Content here, content here.</p>
    </div>
    <div class="stat" style="left:145px">
      <svg width="54" height="54" viewBox="0 0 54 54" style="left:10px;top:0"><circle cx="27" cy="27" r="25" fill="none" stroke="#17a89a" stroke-width="1.8" stroke-dasharray="95 62" transform="rotate(-100 27 27)"/></svg>
      <div class="pct" style="left:10px">30%</div>
      <p>It is a long established fact that a reader will be distracted by the readable content of a page. The point of using Lorem Ipsum is that it has a more-or-less distribution of letters, as opposed to using 'Content here, content here.</p>
    </div>
    <div class="stat" style="left:259px">
      <svg width="54" height="54" viewBox="0 0 54 54" style="left:10px;top:0"><circle cx="27" cy="27" r="25" fill="none" stroke="#17a89a" stroke-width="1.8" stroke-dasharray="100 57" transform="rotate(-90 27 27)"/></svg>
      <div class="pct" style="left:10px">30%</div>
      <p>It is a long established fact that a reader will be distracted by the readable content of a page. The point of using Lorem Ipsum is that it has a more-or-less distribution of letters, as opposed to using 'Content here, content here.</p>
    </div>
    <div class="footer-rule"></div><div class="page-no">4</div>
  </section>

  <section class="slide slide--teal" style="left:810px;top:468px" role="img" aria-label="Teal section slide with faint connected-node network pattern">
    <div class="top-strip"><span></span><span></span><span></span></div>
    <div class="band"><h2>Presentation Title</h2><p>Subtitle</p></div>
    <div class="page-plain">3</div>
  </section>

  <section class="slide slide--teal" style="left:418px;top:761px" role="img" aria-label="Teal closing slide with faint connected-node network pattern">
    <div class="top-strip"><span></span><span></span><span></span></div>
    <div class="thanks">Thank You</div>
    <div class="thanks-bar"><span></span><span></span><span></span></div>
  </section>

</div>
</body>
</html>
```